LITTLE DESIGN WORK REQUIRED!

UPDATE: WE WEREN'T OVERLY ECSTATIC WITH THE DESIGNS WE WERE RECEIVING SO WE DID MOST OF THE DESIGN WORK OURSELVES...

PLEASE SEE THE NEWLY ATTACHED PPT DOC TO VIEW NEARLY EXACT REPLICAS OF WHAT WE WANT THE SITE TO LOOK LIKE. WE NOW NEED YOUR HELP TO MAKE IT LOOK LIKE SOMETHING WORTHY OF THE WEB.

NO CODING REQUIRED - EXPECTED OUTPUT PSD FILES

Hi everyone!

We're looking for a designer to work their magic for our site! We're a not-for-profit program aimed at helping young people realise their potential!

In the attached PPT file, you'll notice we've already DESIGNED THE ENTIRE SITE IN POWERPOINT. Now, we need YOU to make the small changes we requested in the document as well as design the whole thing in psd.

Any questions, don't hesitate to ask.

Brook-Rise
Updates

We've done about 95% of the design for you. Please fine-tune it. See the newly attached PPT doc for details. 

The best two designs will win. This project closes on Friday - please message us if you are absolutely sure you cannot make the deadline.

Thanks,
Brook-Rise

```html
<!DOCTYPE html>
<html lang="en">
<head>
<meta charset="utf-8">
<title>Brook-Rise</title>
<link rel="stylesheet" href="https://fonts.googleapis.com/css2?family=Arimo:ital,wght@0,400;0,700;1,700&display=swap">
<style>
:root{
  --bg-top:#8fc454;
  --bg-mid:#84c99a;
  --bg-bottom:#9fd6de;
  --dark:#3b3b3b;
  --white:#ffffff;
  --green:#1ec51e;
  --green-soft:#7cc243;
  --grey-light:#efefef;
  --grey-text:#9a9a9a;
  --text:#333333;
  --body-text:#555555;
  --sky:#9cc1df;
  --grass:#7c8a4a;
  --touch:#6ec8d6;
  --popular:#78c1ae;
  --ambass:#a9c96e;
}
*{box-sizing:border-box;margin:0;padding:0}
html,body{width:853px;height:1200px;overflow:hidden}
body{
  font-family:"Arimo",Arial,sans-serif;
  background:linear-gradient(180deg,var(--bg-top) 0%,var(--bg-top) 20%,var(--bg-mid) 45%,var(--bg-bottom) 70%,var(--bg-bottom) 100%);
  position:relative;color:var(--text);
}
.page{position:absolute;left:100px;top:54px;width:653px;height:1138px;background:var(--dark)}
.header{position:absolute;left:0;top:0;width:653px;height:78px;background:linear-gradient(180deg,#e9e9e9 0%,#ffffff 45%,#ffffff 100%)}
.brand{position:absolute;left:14px;top:27px;display:flex;align-items:center;gap:8px}
.brand-dot{width:22px;height:22px;border-radius:50%;background:var(--green-soft)}
.brand-name{font-size:26px;font-weight:700;color:#1d1d1d;letter-spacing:-0.5px}
.search{position:absolute;left:413px;top:30px;display:flex}
.search-field{width:189px;height:25px;border:1px solid #d6d6d6;border-radius:3px 0 0 3px;background:#fff;font-size:7px;color:#aaa;padding:8px 7px 0}
.search-btn{width:30px;height:25px;background:#3a3a3a;border-radius:0 4px 4px 0;display:flex;align-items:center;justify-content:center}
.nav{position:absolute;left:14px;top:78px;width:625px;height:46px;display:flex}
.nav a{display:block;height:46px;line-height:46px;font-size:10px;color:#fff;text-decoration:none;text-align:center}
.nav .current{width:114px;background:var(--green)}
.nav .n1{width:100px}.nav .n2{width:100px}.nav .n3{width:104px}.nav .n4{width:80px}
.content{position:absolute;left:14px;top:126px;width:625px;height:939px;background:#fff;overflow:hidden}
.hero-photo{position:absolute;left:0;top:0;width:417px;height:204px;background:linear-gradient(180deg,var(--sky) 0%,#c9dbe9 45%,var(--grass) 62%,#6d7a3f 100%)}
.hero-photo::after{content:"";position:absolute;right:0;top:0;width:120px;height:100%;background:linear-gradient(90deg,rgba(255,255,255,0),rgba(225,236,244,.85))}
.hero-panel{position:absolute;left:420px;top:0;width:205px;height:204px;background:var(--green);text-align:center}
.hero-title{font-size:30px;font-weight:700;color:#fff;margin-top:14px}
.hero-icon{width:72px;height:62px;margin:10px auto 0;background:linear-gradient(180deg,#d9e8f4,#9cb6cc);border-radius:4px}
.hero-btn{position:absolute;left:22px;top:136px;width:165px;height:50px;border:2px solid #bff0bf;border-radius:3px;background:linear-gradient(180deg,#34b03a,#158f19);color:#fff;font-size:15px;line-height:18px;padding-top:6px}
.slider-dots{position:absolute;left:10px;top:210px;display:flex;gap:4px}
.slider-dots span{width:17px;height:17px;border-radius:50%;background:var(--green-soft)}
.slider-dots .on{background:#cfcfcf}
.rule{position:absolute;left:0;top:233px;width:625px;height:1px;background:#e6e6e6}
.intro{position:absolute;left:11px;top:251px;width:410px;font-size:8px;line-height:10px;color:var(--body-text)}
.intro p{margin-bottom:7px}
.intro b{color:#222}
.steps{position:absolute;left:12px;top:315px}
.steps text{font-family:"Arimo",Arial,sans-serif;font-size:12px}
.section-title{position:absolute;left:12px;top:377px;font-size:16px;font-weight:400;line-height:18px;color:#333}
.category{position:absolute;left:12px;top:402px;width:382px;height:17px;background:linear-gradient(180deg,#9bd45f,#6fb82f);color:#fff;font-size:12px;line-height:17px;padding-left:5px}
.posts{position:absolute;left:16px;top:434px;width:380px}
.post{height:94.4px}
.post-title{font-size:9px;color:#333;height:15px}
.post-body{display:flex;gap:7px}
.post-pic{flex:none;width:80px;height:62px;background:#f2f0f0;border:1px solid #dcdcdc;display:flex;align-items:center;justify-content:center;font-size:9px;color:#555}
.post-text{width:291px;font-size:8px;line-height:12px;color:var(--body-text);padding-top:3px}
.card{position:absolute;left:439px;width:177px;border:2px solid #e8e8e8;color:#fff;overflow:hidden}
.card::before{content:"";position:absolute;left:-2px;top:-2px;width:177px;height:10px;background:linear-gradient(180deg,#f6f6f6,#fff)}
.card::after{content:"";position:absolute;left:10px;top:8px;border-left:9px solid transparent;border-right:9px solid transparent;border-top:7px solid #fff}
.card h3{font-size:19px;font-weight:400;margin:23px 0 0 13px;line-height:22px;text-shadow:0 1px 2px rgba(0,0,0,.25)}
.card-touch{top:249px;height:156px;background:var(--touch)}
.touch-art{position:absolute;left:35px;top:50px;width:102px;height:100px;background:linear-gradient(180deg,#3b5f9e 0%,#3b5f9e 32%,#dfe6ee 32%,#b9c6d2 100%);border-radius:4px}
.card-popular{top:421px;height:156px;background:var(--popular)}
.pop-list{margin:17px 0 0 16px}
.pop-item{display:flex;gap:9px;height:45px}
.pop-num{width:32px;height:32px;background:#fff;border:1px solid #9ccfc2;color:#2a7f6d;font-size:15px;text-align:center;line-height:31px;border-radius:2px}
.pop-meta{font-size:7.5px;font-weight:700;line-height:11px;padding-top:2px}
.pop-meta span{display:block;margin-top:8px}
.card-ambass{top:595px;height:155px;background:var(--ambass)}
.amb-list{margin:11px 0 0 16px}
.amb{display:flex;gap:7px;height:42px}
.amb-pic{width:33px;height:31px;background:linear-gradient(180deg,#f4f4f4,#d9d9d9);border:1px solid #fff}
.amb-meta{font-size:7.5px;font-weight:700;line-height:11.5px}
.amb-meta i{display:block}
.more{font-size:7.5px;font-weight:700;margin:2px 0 0 20px}
.footer-copy{position:absolute;left:16px;top:1102px;font-size:7px;color:#fff}
.footer-contact{position:absolute;right:18px;top:1099px;font-size:7px;color:#fff}
</style>
</head>
<body>
<div class="page">
  <header class="header">
    <div class="brand"><span class="brand-dot"></span><span class="brand-name">Brook-Rise</span></div>
    <div class="search">
      <div class="search-field">Enter Keyword</div>
      <div class="search-btn"><svg width="14" height="14" viewBox="0 0 14 14"><circle cx="5.5" cy="5.5" r="4" fill="none" stroke="#fff" stroke-width="1.8"/><line x1="8.5" y1="8.5" x2="13" y2="13" stroke="#fff" stroke-width="2"/></svg></div>
    </div>
  </header>
  <nav class="nav">
    <a class="current" href="#">About Us</a>
    <a class="n1" href="#">Resources</a>
    <a class="n2" href="#">Workshops</a>
    <a class="n3" href="#">Ambassadors</a>
    <a class="n4" href="#">Feats</a>
  </nav>
  <main class="content">
    <div class="hero-photo" role="img" aria-label="Photograph of elephants on grassland under a cloudy sky"></div>
    <div class="hero-panel">
      <div class="hero-title">Kilimanjaro</div>
      <div class="hero-icon" role="img" aria-label="Illustration of a sign-up form with a pencil"></div>
      <div class="hero-btn">Sign-up for our<br>Brook-Rise Feats.</div>
    </div>
    <div class="slider-dots"><span class="on"></span><span></span><span></span><span></span></div>
    <div class="rule"></div>
    <section class="intro">
      <p><b>Brook-Rise</b> is a not-for-profit program aimed at helping people – especially young people – realise their potential and achieve success.</p>
      <p><b>Our resources</b> are categorised into four areas: discovery, design, build, and achieve – what we believe are the four steps in the achievement framework we teach.</p>
    </section>
    <svg class="steps" width="390" height="52" viewBox="0 0 390 52">
      <polygon points="0,0 84,0 96,25 84,50 0,50" fill="#efefef"/>
      <polygon points="93,0 177,0 189,25 177,50 93,50 105,25" fill="#7cc243"/>
      <polygon points="186,0 270,0 282,25 270,50 186,50 198,25" fill="#efefef"/>
      <polygon points="279,0 363,0 375,25 363,50 279,50 291,25" fill="#efefef"/>
      <text x="48" y="30" text-anchor="middle" fill="#9a9a9a">Discover</text>
      <text x="145" y="30" text-anchor="middle" fill="#fff">Design</text>
      <text x="238" y="30" text-anchor="middle" fill="#9a9a9a">Build</text>
      <text x="331" y="30" text-anchor="middle" fill="#9a9a9a">Achieve</text>
    </svg>
    <h2 class="section-title">Recent Posts</h2>
    <div class="category">Design</div>
    <section class="posts">
      <article class="post"><div class="post-title">Title A</div><div class="post-body"><div class="post-pic">Picture A</div><p class="post-text">Lorem ipsum dosectetur adipisicing elit, sed do. Lorem ipsum dosectetur adipisicing elit, sed do. Lorem ipsum dosectetur adipisicing elit, sed do. Lorem ipsum dosectetur adipisicing elit, sed do. Lorem ipsum dosectetur adipisicing elit, sed do. Lorem ipsum dosectetur adipisicing elit, sed do. Lorem ipsum dosectetur adipisicing elit.</p></div></article>
      <article class="post"><div class="post-title">Title B</div><div class="post-body"><div class="post-pic">Picture B</div><p class="post-text">Lorem ipsum dosectetur adipisicing elit, sed do. Lorem ipsum dosectetur adipisicing elit, sed do. Lorem ipsum dosectetur adipisicing elit, sed do. Lorem ipsum dosectetur adipisicing elit, sed do. Lorem ipsum dosectetur adipisicing elit, sed do. Lorem ipsum dosectetur adipisicing elit, sed do. Lorem ipsum dosectetur adipisicing elit.</p></div></article>
      <article class="post"><div class="post-title">Title C</div><div class="post-body"><div class="post-pic">Picture C</div><p class="post-text">Lorem ipsum dosectetur adipisicing elit, sed do. Lorem ipsum dosectetur adipisicing elit, sed do. Lorem ipsum dosectetur adipisicing elit, sed do. Lorem ipsum dosectetur adipisicing elit, sed do. Lorem ipsum dosectetur adipisicing elit, sed do. Lorem ipsum dosectetur adipisicing elit, sed do. Lorem ipsum dosectetur adipisicing elit.</p></div></article>
      <article class="post"><div class="post-title">Title D</div><div class="post-body"><div class="post-pic">Picture D</div><p class="post-text">Lorem ipsum dosectetur adipisicing elit, sed do. Lorem ipsum dosectetur adipisicing elit, sed do. Lorem ipsum dosectetur adipisicing elit, sed do. Lorem ipsum dosectetur adipisicing elit, sed do. Lorem ipsum dosectetur adipisicing elit, sed do. Lorem ipsum dosectetur adipisicing elit, sed do. Lorem ipsum dosectetur adipisicing elit.</p></div></article>
      <article class="post"><div class="post-title">Title E</div><div class="post-body"><div class="post-pic">Picture E</div><p class="post-text">Lorem ipsum dosectetur adipisicing elit, sed do. Lorem ipsum dosectetur adipisicing elit, sed do. Lorem ipsum dosectetur adipisicing elit, sed do. Lorem ipsum dosectetur adipisicing elit, sed do. Lorem ipsum dosectetur adipisicing elit, sed do. Lorem ipsum dosectetur adipisicing elit, sed do. Lorem ipsum dosectetur adipisicing elit.</p></div></article>
    </section>
    <aside class="card card-touch">
      <h3>Get in touch</h3>
      <div class="touch-art" role="img" aria-label="Illustration of a small storefront with an awning"></div>
    </aside>
    <aside class="card card-popular">
      <h3>What’s popular?</h3>
      <div class="pop-list">
        <div class="pop-item"><div class="pop-num">1</div><div class="pop-meta">Lorem ipsum dolor<span>3,312,123 views</span></div></div>
        <div class="pop-item"><div class="pop-num">2</div><div class="pop-meta">Lorem ipsum dolor<span>3,312,123 views</span></div></div>
      </div>
    </aside>
    <aside class="card card-ambass">
      <h3>Ambassadors</h3>
      <div class="amb-list">
        <div class="amb"><div class="amb-pic" role="img" aria-label="Profile photo placeholder"></div><div class="amb-meta">John Doe<i>Young entrepreneur</i>» Meet John</div></div>
        <div class="amb"><div class="amb-pic" role="img" aria-label="Profile photo placeholder"></div><div class="amb-meta">Jane Smith<i>Pro athlete</i>» Meet Jane</div></div>
      </div>
      <div class="more">» Brook-Rise ambassadors</div>
    </aside>
  </main>
  <div class="footer-copy">Copyright © 2012 brookrise. All Rights Reserved</div>
  <div class="footer-contact">Contact : Brook-Rise, Lorem street, Phone : 91-04417-530862, Email : info@brookrise.com</div>
</div>
</body>
</html>
```